CoverBeacon Gap Insurance InfoGraphic

We need an infographic detailing what Gap insurance is, the types, and who needs it. All of this information can be found in the attached report. Please adhere to the same branding style as our website, www.coverbeacon-example.com

Target Market(s)

people age 64+ and their families

Industry/Entity Type

Insurance

Requirements
Must have
• Must cover multiple facets of gap insurance, not just "what is it"

```html
<!DOCTYPE html>
<html lang="en">
<head>
<meta charset="utf-8">
<title>CoverBeacon – Medigap Insurance Guide</title>
<link href="https://fonts.googleapis.com/css2?family=Ubuntu:wght@500&display=swap" rel="stylesheet">
<style>
  :root{
    --navy:#022235;
    --ink:#0e2235;
    --orange:#ff8200;
    --plum-dark:#4a0030;
    --plum-mid:#7e0b55;
    --plum-edge:#8d1565;
    --red-dot:#c8202e;
    --white:#ffffff;
  }
  html,body{margin:0;padding:0;overflow:hidden;background:var(--white);}
  .canvas{width:923px;height:1200px;display:block;}
  svg text{font-family:"Ubuntu",sans-serif;font-weight:500;}
  .label{fill:var(--white);font-size:32px;text-anchor:middle;dominant-baseline:central;}
  .label-lg{font-size:52px;}
  .chip-text{fill:var(--white);font-size:17px;text-anchor:middle;dominant-baseline:central;}
  .hex-title{fill:var(--white);font-size:48px;text-anchor:middle;}
  .body{fill:var(--ink);font-size:32px;}
  .center{text-anchor:middle;}
  .price{fill:var(--ink);font-size:40px;}
  .answer{fill:var(--ink);font-size:34px;text-anchor:middle;dominant-baseline:central;}
  .navy{fill:var(--navy);}
  .orange{fill:var(--orange);}
  .dot{fill:var(--red-dot);}
  .box{fill:url(#plum);stroke:var(--plum-edge);stroke-width:3;}
  .frame{fill:url(#frame);}
</style>
</head>
<body>
<svg class="canvas" viewBox="0 0 1680 2184" xmlns="http://www.w3.org/2000/svg">
  <defs>
    <linearGradient id="plum" x1="0" x2="1" y1="0" y2="0">
      <stop offset="0" stop-color="var(--plum-dark)"/>
      <stop offset="0.5" stop-color="var(--plum-mid)"/>
      <stop offset="1" stop-color="var(--plum-dark)"/>
    </linearGradient>
    <linearGradient id="ruby" x1="0" y1="0" x2="0.6" y2="1">
      <stop offset="0" stop-color="#c06a78"/>
      <stop offset="0.45" stop-color="#a01e34"/>
      <stop offset="0.75" stop-color="#c8243a"/>
      <stop offset="1" stop-color="#8a1426"/>
    </linearGradient>
    <linearGradient id="sky" x1="0" y1="0" x2="0" y2="1">
      <stop offset="0" stop-color="#5fa0c8"/>
      <stop offset="0.5" stop-color="#2a86c0"/>
      <stop offset="1" stop-color="#1266a8"/>
    </linearGradient>
    <linearGradient id="frame" x1="0" y1="0" x2="1" y2="1">
      <stop offset="0" stop-color="#ffffff"/>
      <stop offset="0.5" stop-color="#b5b5b5"/>
      <stop offset="1" stop-color="#f2f2f2"/>
    </linearGradient>
    <linearGradient id="stem" x1="0" y1="0" x2="0" y2="1">
      <stop offset="0" stop-color="#4a0030"/>
      <stop offset="1" stop-color="#8a0e5c"/>
    </linearGradient>
    <linearGradient id="redStem" x1="0" y1="0" x2="0" y2="1">
      <stop offset="0" stop-color="#a01e34"/>
      <stop offset="1" stop-color="#d42a3e"/>
    </linearGradient>
  </defs>

  <!-- Title hexagon -->
  <g class="title-hex">
    <polygon class="frame" points="612,212 717,32 922,32 1026,212 922,390 717,390"/>
    <polygon fill="url(#ruby)" stroke="#c8243a" stroke-width="3" points="648,212 735,62 907,62 992,212 907,360 735,360"/>
    <text class="hex-title" x="818" y="198">Medigap</text>
    <text class="hex-title" x="818" y="256">Insurance</text>
  </g>

  <!-- Branch arrows -->
  <g class="navy">
    <rect x="100" y="295" width="518" height="32"/>
    <rect x="100" y="295" width="32" height="66"/>
    <polygon points="74,358 158,358 116,422"/>
    <rect x="1014" y="295" width="516" height="32"/>
    <rect x="1498" y="295" width="32" height="66"/>
    <polygon points="1472,358 1556,358 1514,422"/>
  </g>

  <!-- Question row -->
  <polygon class="box" points="62,474 465,474 494,525 465,577 62,577 32,525"/>
  <text class="label" x="263" y="525">Medigap Pays For?</text>
  <polygon class="box" points="612,474 1016,474 1045,525 1016,577 612,577 582,525"/>
  <text class="label" x="814" y="525">When Can Buy?</text>
  <polygon class="box" points="1155,474 1559,474 1588,525 1559,577 1155,577 1125,525"/>
  <text class="label" x="1356" y="525">Conditions For Obtaining?</text>

  <!-- Pays for list -->
  <rect class="navy" x="66" y="593" width="10" height="177"/>
  <circle class="dot" cx="71" cy="655" r="12"/>
  <circle class="dot" cx="71" cy="713" r="12"/>
  <circle class="dot" cx="71" cy="771" r="12"/>
  <text class="body" x="117" y="666">Deductibles</text>
  <text class="body" x="117" y="724">Co-Insurance</text>
  <text class="body" x="117" y="782">Co-Payments, and more</text>

  <!-- When can buy -->
  <rect fill="url(#stem)" x="795" y="577" width="37" height="48"/>
  <polygon fill="url(#stem)" points="766,623 861,623 814,695"/>
  <text class="body center" x="808" y="734">During 6 month</text>
  <text class="body center" x="812" y="777">Medigap open period</text>

  <!-- Conditions list -->
  <rect class="navy" x="1157" y="593" width="10" height="207"/>
  <circle class="dot" cx="1162" cy="655" r="12"/>
  <circle class="dot" cx="1162" cy="713" r="12"/>
  <circle class="dot" cx="1162" cy="808" r="12"/>
  <text class="body" x="1207" y="666">Your age 65</text>
  <text class="body" x="1207" y="724">You are enrolled in medicare</text>
  <text class="body" x="1207" y="766">Parts A &amp; B</text>
  <text class="body" x="1207" y="819">You are disabled and under</text>
  <text class="body" x="1207" y="862">the age of 65</text>

  <!-- Already have plan -->
  <polygon class="box" points="614,849 1018,849 1047,900 1018,951 614,951 584,900"/>
  <text class="label" x="815" y="900">Already have Plan?</text>
  <rect fill="url(#stem)" x="803" y="951" width="23" height="12"/>
  <polygon fill="url(#stem)" points="788,962 840,962 814,1000"/>

  <g class="orange">
    <rect x="458" y="1015" width="644" height="31"/>
    <polygon points="398,1030 460,990 460,1071"/>
    <polygon points="1162,1030 1100,990 1100,1071"/>
  </g>

  <!-- Yes / No -->
  <polygon class="frame" points="175,1025 222,943 318,943 365,1025 318,1108 222,1108"/>
  <polygon fill="url(#sky)" stroke="#3ab0e0" stroke-width="3" points="190,1025 230,957 310,957 350,1025 310,1094 230,1094"/>
  <text class="answer" x="270" y="1026">Yes</text>
  <polygon class="frame" points="1201,1025 1248,943 1344,943 1391,1025 1344,1108 1248,1108"/>
  <polygon fill="url(#sky)" stroke="#3ab0e0" stroke-width="3" points="1216,1025 1256,957 1336,957 1376,1025 1336,1094 1256,1094"/>
  <text class="answer" x="1296" y="1026">No</text>

  <g class="orange">
    <rect x="244" y="1122" width="31" height="88"/>
    <polygon points="219,1208 300,1208 260,1270"/>
    <rect x="1278" y="1122" width="31" height="88"/>
    <polygon points="1252,1208 1333,1208 1293,1270"/>
  </g>

  <!-- Sample pricing -->
  <text class="price center" x="832" y="1112">Sample Pricing</text>
  <rect class="navy" x="686" y="1148" width="10" height="252"/>
  <circle class="dot" cx="691" cy="1148" r="11"/>
  <circle class="dot" cx="691" cy="1199" r="11"/>
  <circle class="dot" cx="691" cy="1250" r="11"/>
  <circle class="dot" cx="691" cy="1300" r="11"/>
  <circle class="dot" cx="691" cy="1350" r="11"/>
  <circle class="dot" cx="691" cy="1400" r="11"/>
  <text class="price" x="737" y="1164">A: $172.75</text>
  <text class="price" x="737" y="1215">B: $187.84</text>
  <text class="price" x="737" y="1266">C: $233.21</text>
  <text class="price" x="737" y="1316">K: $100.21</text>
  <text class="price" x="737" y="1366">L: $144.33</text>
  <text class="price" x="737" y="1416">N: $139.41</text>

  <!-- Yes / No outcomes -->
  <polygon class="box" points="64,1287 468,1287 497,1338 468,1390 64,1390 34,1338"/>
  <text class="label" x="265" y="1338">Medical Treatment?</text>
  <polygon class="box" points="1098,1287 1501,1287 1530,1338 1501,1390 1098,1390 1068,1338"/>
  <text class="label" x="1299" y="1338">Choose a plan</text>
  <rect fill="url(#stem)" x="1287" y="1390" width="25" height="12"/>
  <polygon fill="url(#stem)" points="1265,1402 1333,1402 1299,1452"/>

  <!-- Plan chips -->
  <g class="plans">
    <polygon class="box" points="1046,1474 1114,1474 1130,1502 1114,1530 1046,1530 1030,1502"/>
    <text class="chip-text" x="1080" y="1502">Plan A</text>
    <polygon class="box" points="1156,1474 1224,1474 1240,1502 1224,1530 1156,1530 1140,1502"/>
    <text class="chip-text" x="1190" y="1502">Plan B</text>
    <polygon class="box" points="1266,1474 1334,1474 1350,1502 1334,1530 1266,1530 1250,1502"/>
    <text class="chip-text" x="1300" y="1502">Plan C</text>
    <polygon class="box" points="1376,1474 1444,1474 1460,1502 1444,1530 1376,1530 1360,1502"/>
    <text class="chip-text" x="1410" y="1502">Plan D</text>
    <polygon class="box" points="1486,1474 1554,1474 1570,1502 1554,1530 1486,1530 1470,1502"/>
    <text class="chip-text" x="1520" y="1502">Plan F</text>
    <polygon class="box" points="1046,1556 1114,1556 1130,1583 1114,1611 1046,1611 1030,1583"/>
    <text class="chip-text" x="1080" y="1583">Plan G</text>
    <polygon class="box" points="1156,1556 1224,1556 1240,1583 1224,1611 1156,1611 1140,1583"/>
    <text class="chip-text" x="1190" y="1583">Plan K</text>
    <polygon class="box" points="1266,1556 1334,1556 1350,1583 1334,1611 1266,1611 1250,1583"/>
    <text class="chip-text" x="1300" y="1583">Plan L</text>
    <polygon class="box" points="1376,1556 1444,1556 1460,1583 1444,1611 1376,1611 1360,1583"/>
    <text class="chip-text" x="1410" y="1583">Plan M</text>
    <polygon class="box" points="1486,1556 1554,1556 1570,1583 1554,1611 1486,1611 1470,1583"/>
    <text class="chip-text" x="1520" y="1583">Plan N</text>
  </g>

  <!-- Path to two steps -->
  <g class="navy">
    <rect x="243" y="1415" width="33" height="175"/>
    <rect x="243" y="1558" width="320" height="32"/>
    <polygon points="560,1532 560,1616 624,1574"/>
  </g>

  <polygon class="frame" points="666,1572 743,1440 893,1440 970,1572 893,1703 743,1703"/>
  <polygon fill="url(#ruby)" stroke="#c8243a" stroke-width="3" points="692,1572 755,1462 881,1462 944,1572 881,1681 755,1681"/>
  <text class="label" x="818" y="1572">2 Steps</text>
  <rect fill="url(#redStem)" x="800" y="1681" width="37" height="46"/>
  <polygon fill="url(#redStem)" points="770,1725 866,1725 818,1797"/>

  <text class="body" x="220" y="1716">1st Step &gt;</text>
  <text class="body" x="1267" y="1716">2nd Step &gt;</text>

  <polygon class="box" points="79,1770 509,1770 538,1824 509,1879 79,1879 49,1824"/>
  <text class="label" x="294" y="1824">Medicare coverage approves</text>
  <polygon class="box" points="1129,1770 1559,1770 1588,1824 1559,1879 1129,1879 1099,1824"/>
  <text class="label" x="1340" y="1803">Go to your Medigap</text>
  <text class="label" x="1343" y="1845">Insurance Plan</text>

  <g class="navy">
    <rect x="630" y="1810" width="376" height="32"/>
    <polygon points="568,1826 632,1784 632,1868"/>
    <polygon points="1068,1826 1004,1784 1004,1868"/>
  </g>

  <!-- Final result -->
  <polygon class="box" points="478,1985 1100,1985 1142,2063 1100,2142 478,2142 433,2063"/>
  <text class="label label-lg" x="788" y="2063">Recieve your rest of Bill</text>
  <g class="navy">
    <rect x="1520" y="1905" width="33" height="175"/>
    <rect x="1234" y="2048" width="319" height="32"/>
    <polygon points="1172,2063 1236,2021 1236,2105"/>
  </g>
</svg>
</body>
</html>
```